Business Card for Multi-Brand Sportswear Company

We are looking for a business card which represents our company and the multiple brands within it.

The company: Kelt Athletic (LTD)
The brands: Kelt, PawaLuni, VerdantFlex, Grit and Gale

Employees using these cards would be representing Kelt Athletic, rather than any of the individual brands. You will see a current design within the uploaded files, to give some inspiration. The actual text of the brands is not necessary, but the logos should be on there is some format.

Our creative minds on this are stretched, so we are looking for someone to make this their own, and show us what a good business card should look like.

We may like to get these printed with spot gloss, so keep that in mind with your designs.

www.keltathletic.co.uk

Industry/Entity Type

Business

Contact Information for Business Card

Tom Hollingsworth-Pryce
Operations Manager
(+44) 1632 960 418
Tom@keltathletic.co.uk
www.keltathletic.co.uk

Font styles to use
Sans Serif
Other font styles liked:
• Eurostile

Colors
ffffff

Requirements
Nice to have
• Dark (black) background

```html
<!DOCTYPE html>
<html lang="en">
<head>
<meta charset="utf-8">
<title>Kelt Athletic — Business Card</title>
<link href="https://fonts.googleapis.com/css2?family=Michroma&family=Montserrat:wght@400;500;700&display=swap" rel="stylesheet">
<style>
  :root{
    --bg-top:#5a5a5a;
    --bg-bottom:#8e8e8e;
    --card-white:#f7f7f7;
    --ink:#141414;
    --dark:#232323;
    --red:#e3202a;
    --grey-text:#6e6e6e;
    --facet:#e2e2e2;
    --purple:#5b4a63;
    --soft-grey:#9a9a9a;
    --light-text:#e8e8e8;
  }
  *{box-sizing:border-box;margin:0;padding:0}
  html,body{width:1200px;height:1200px;overflow:hidden}
  body{
    background:linear-gradient(180deg,var(--bg-top),var(--bg-bottom));
    font-family:"Montserrat",sans-serif;
    position:relative;
  }
  .card{
    position:absolute;left:220px;width:760px;height:434px;
    border-radius:14px;overflow:hidden;
    background:var(--card-white);
    box-shadow:0 18px 40px rgba(0,0,0,.35);
  }
  .card--front{top:110px}
  .card--back{top:650px}

  .wordmark{font-family:"Michroma",sans-serif;color:var(--ink);letter-spacing:.02em;display:flex;align-items:center;gap:14px}
  .wordmark__mark{width:22px;height:22px;background:var(--red);border-radius:50%;flex:none}

  /* front */
  .front__top{position:absolute;inset:0 0 auto 0;height:188px;padding:56px 44px 0 44px;display:flex;justify-content:space-between;align-items:flex-start}
  .front__top .wordmark{font-size:28px}
  .person{text-align:right}
  .person__name{font-size:28px;color:var(--ink)}
  .person__name b{font-weight:700}
  .person__role{font-size:17px;color:var(--grey-text);margin-top:6px}
  .front__bottom{position:absolute;left:0;right:0;top:188px;bottom:0;background:var(--dark)}
  .red-strip{position:absolute;left:44px;right:44px;height:10px;background:var(--red);border-radius:0 0 8px 8px}
  .red-strip--top{top:0}
  .red-strip--bottom{bottom:0;height:16px;border-radius:8px 8px 0 0}
  .address{position:absolute;left:44px;top:34px;color:var(--light-text);font-size:15px;line-height:30px}
  .contacts{position:absolute;right:44px;top:34px;list-style:none;color:var(--light-text);font-size:15px;line-height:30px;text-align:right}
  .contacts li{display:flex;justify-content:flex-end;align-items:center;gap:12px}
  .icon{width:22px;height:22px;flex:none}

  /* back */
  .facets{position:absolute;left:0;right:0;bottom:0;height:60px}
  .back__logo{position:absolute;top:120px;left:0;right:0;display:flex;justify-content:center}
  .back__logo .wordmark{font-size:44px}
  .back__logo .wordmark__mark{width:34px;height:34px}
  .brands{position:absolute;left:50px;right:50px;top:300px;display:flex;justify-content:space-between;align-items:center;list-style:none;font-family:"Michroma",sans-serif;font-size:17px}
  .brand{display:flex;align-items:center;gap:9px}
  .brand__dot{width:14px;height:14px;flex:none}
  .brand--pawaluni{color:var(--purple)} .brand--pawaluni .brand__dot{background:var(--purple);border-radius:3px}
  .brand--grit{color:var(--red)} .brand--grit .brand__dot{background:var(--red)}
  .brand--kelt{color:var(--ink)} .brand--kelt .brand__dot{background:var(--ink);border-radius:50%}
  .brand--verdant{color:var(--soft-grey)} .brand--verdant .brand__dot{border:2px solid var(--soft-grey);border-radius:50%}
</style>
</head>
<body>

<section class="card card--front" aria-label="Business card front">
  <div class="front__top">
    <div class="wordmark"><span class="wordmark__mark"></span>Kelt Athletic</div>
    <div class="person">
      <p class="person__name"><b>Tom</b> Hollingsworth-Pryce</p>
      <p class="person__role">Managing Director</p>
    </div>
  </div>
  <div class="front__bottom">
    <div class="red-strip red-strip--top"></div>
    <address class="address" style="font-style:normal">
      Fernbank Court<br>Ashwick<br>Harrowdale<br>West Marland<br>HD9 4QX
    </address>
    <ul class="contacts">
      <li>+44 (0)1632 960418
        <svg class="icon" viewBox="0 0 22 22"><circle cx="11" cy="11" r="10" fill="none" stroke="#e3202a" stroke-width="2"/><path d="M7.5 6.5l2 0 1 2.5-1.3 1c.6 1.3 1.5 2.2 2.8 2.8l1-1.3 2.5 1v2c-4.5.3-8.3-3.5-8-8z" fill="#fff"/></svg></li>
      <li>tom@keltathletic.co.uk
        <svg class="icon" viewBox="0 0 22 22"><circle cx="11" cy="11" r="10" fill="none" stroke="#e3202a" stroke-width="2"/><rect x="6" y="7.5" width="10" height="7" fill="#fff"/><path d="M6 7.5l5 4 5-4" fill="none" stroke="#232323" stroke-width="1.2"/></svg></li>
      <li>hello@keltathletic.co.uk
        <svg class="icon" viewBox="0 0 22 22"><circle cx="11" cy="11" r="10" fill="none" stroke="#e3202a" stroke-width="2"/><rect x="6" y="7.5" width="10" height="7" fill="#fff"/><path d="M6 7.5l5 4 5-4" fill="none" stroke="#232323" stroke-width="1.2"/></svg></li>
      <li>www.keltathletic.co.uk
        <svg class="icon" viewBox="0 0 22 22"><circle cx="11" cy="11" r="10" fill="none" stroke="#e3202a" stroke-width="2"/><path d="M11 5.5l5.5 5h-1.5v5h-2.5v-3h-3v3h-2.5v-5h-1.5z" fill="#fff"/></svg></li>
    </ul>
    <div class="red-strip red-strip--bottom"></div>
  </div>
</section>

<section class="card card--back" aria-label="Business card back">
  <div class="back__logo">
    <div class="wordmark"><span class="wordmark__mark"></span>Kelt Athletic</div>
  </div>
  <ul class="brands">
    <li class="brand brand--pawaluni"><span class="brand__dot"></span>PawaLuni</li>
    <li class="brand brand--grit"><span class="brand__dot"></span>Grit and Gale</li>
    <li class="brand brand--kelt"><span class="brand__dot"></span>Kelt</li>
    <li class="brand brand--verdant"><span class="brand__dot"></span>VerdantFlex</li>
  </ul>
  <svg class="facets" viewBox="0 0 760 60" preserveAspectRatio="none" aria-hidden="true">
    <polygon points="0,30 180,12 380,34 560,14 760,28 760,60 0,60" fill="#e6e6e6"/>
    <polygon points="0,44 240,30 470,50 760,40 760,60 0,60" fill="#d8d8d8"/>
  </svg>
</section>

</body>
</html>
```